依頼詳細
店頭配布、駅前でのビラ配り等で使用します。
また裏面には求人も載せたいので、
求人内容詳細をわかりやすく、目を引く内容で
デザインして頂きたいですです。
表面は、綺麗で高級感はだしつつ
楽しいお店というのが伝わればと思います。
記載項目
順不同(表面、集客用)
・ロゴ(添付)
・地図
・電話番号043-518-2264
・住所千葉県浦安市北栄2-7-14ミナトコート305
・営業時間OPEN20時~5時
・チケット持参1時間2500円飲み放題!
・飲み放題メニュー
ビール、超炭酸ハイボール、サワー、ソフトドリンク
・カラオケ完備
・各種宴会、二次会にもご利用頂けます!
サイズ
50×160センチ
ページ数
両面
希望イメージ
シンプル 複雑
単色 カラフル
暗い 明るい
日常 高級
遊び心 厳粛
未来的 伝統的
女性的 男性的
希望する色
赤系、青系
納品ファイル
• 高解像度JPG (.jpg)
補足説明
営業時間を20:00〜LASTに変更お願いします。
サイズ50×160mmです。
※サイズですがハガキサイズで縦向きでお願いします。
裏面の求人には、時給2500円〜
エリアNO.1の各種高額バック有
オリジナルTシャツ支給
送迎無料
短時間・長時間シフト自由提出
稼げてシフトも組みやすい
コロナ対策万全なお店
を載せて頂きたいです。
時給と高額バックにインパクトを与えて頂きたいです。
TEL 08052730419
こちらの番号も載せて頂きたいです。
それから添付ファイルのQRコードも
載せて頂きたいです。
■ 選んだ理由

女性らしさと分かりやすさ、それから目を引くと言った点では
完璧でした!
修正時の対応スピードも良かったです。

■ 提案者全員のお礼・コメント

たくさんのご提案を頂きありがとうございました!

```html
<!DOCTYPE html>
<html lang="ja">
<head>
<meta charset="UTF-8">
<title>Stella Girls Bar – 飲み放題フライヤー</title>
<link rel="stylesheet" href="https://fonts.googleapis.com/css2?family=Noto+Serif+JP:wght@400;600;700&family=Playfair+Display:wght@700&display=swap">
<style>
  :root {
    --bg: #050404;
    --gold: #e9c46a;
    --gold-deep: #b8862b;
    --gold-glow: rgba(255, 196, 80, 0.75);
    --white: #f4f1ea;
    --red: #d9262b;
    --map-tone: #d8d4cc;
    --figure-tone: #d9d3c6;
    --leaf-tone: #8a6420;
  }
  * { margin: 0; padding: 0; box-sizing: border-box; }
  html, body { width: 800px; height: 1200px; overflow: hidden; background: var(--bg); }
  .flyer {
    position: relative;
    width: 800px;
    height: 1200px;
    overflow: hidden;
    background:
      radial-gradient(ellipse 420px 200px at 50% 60px, rgba(201, 150, 60, 0.35), transparent 70%),
      var(--bg);
    font-family: "Noto Serif JP", serif;
    color: var(--white);
  }
  .gold-dust {
    position: absolute; left: 0; top: 0; width: 800px; height: 300px;
    background: radial-gradient(ellipse at 50% 10%, rgba(233, 196, 106, 0.25), transparent 65%);
  }
  .leaf {
    position: absolute;
    background: radial-gradient(ellipse at center, var(--leaf-tone), rgba(138, 100, 32, 0) 70%);
  }
  .leaf--top-left { left: -20px; top: 90px; width: 190px; height: 200px; }
  .leaf--top-right { right: -30px; top: 30px; width: 170px; height: 170px; }
  .leaf--mid-right { right: -20px; top: 520px; width: 170px; height: 220px; }
  .leaf--mid-left { left: -20px; top: 630px; width: 170px; height: 180px; }
  .leaf--bottom-right { right: 60px; top: 770px; width: 140px; height: 120px; }

  .brand {
    position: absolute; left: 0; top: 90px; width: 800px;
    text-align: center;
  }
  .brand__name {
    font-weight: 700; font-size: 64px; color: var(--gold); letter-spacing: 3px;
  }
  .brand__mark {
    display: inline-block; width: 22px; height: 22px; border-radius: 50%;
    background: var(--gold); margin-left: 14px; vertical-align: middle;
  }

  .offer-lead {
    position: absolute; left: 0; top: 310px; width: 800px;
    text-align: center; font-size: 58px; font-weight: 400; letter-spacing: 4px;
  }
  .offer-price {
    position: absolute; left: 0; top: 430px; width: 800px;
    text-align: center;
    font-family: "Playfair Display", serif; font-weight: 700; font-size: 112px;
    color: #ffe9a8;
    text-shadow: 0 0 12px var(--gold-glow), 0 0 28px var(--gold-glow), 0 0 50px rgba(255, 170, 40, 0.5);
  }
  .offer-rule {
    position: absolute; left: 130px; top: 575px; width: 540px; height: 3px;
    background: linear-gradient(90deg, transparent, var(--gold) 15%, var(--gold) 85%, transparent);
  }

  .menu { position: absolute; left: 0; top: 690px; width: 800px; text-align: center; }
  .menu__title { font-size: 36px; letter-spacing: 3px; margin-bottom: 12px; }
  .menu__item { font-size: 29px; line-height: 46px; }

  .figure {
    position: absolute; left: 672px; top: 650px; width: 98px; height: 270px;
    background: linear-gradient(180deg, var(--figure-tone), #9a9387);
    border-radius: 40px 40px 12px 12px;
    opacity: 0.8;
  }

  .map {
    position: absolute; left: 0; top: 920px; width: 362px; height: 280px;
    background: var(--map-tone);
  }

  .info { position: absolute; left: 362px; top: 925px; width: 438px; text-align: center; }
  .info__hours { font-size: 44px; font-weight: 400; letter-spacing: 1px; color: var(--white); }
  .info__karaoke { font-size: 40px; font-weight: 600; color: var(--gold); margin-top: 4px; }
  .info__contact-lead { font-size: 22px; color: var(--gold); margin-top: 4px; }
  .info__tel { font-size: 38px; font-weight: 600; color: var(--gold); margin-top: 10px; letter-spacing: 1px; }
  .info__address { font-size: 19px; color: var(--white); margin-top: 4px; }
</style>
</head>
<body>
<main class="flyer">
  <div class="gold-dust"></div>
  <div class="leaf leaf--top-left" role="img" aria-label="金色の葉の装飾"></div>
  <div class="leaf leaf--top-right" role="img" aria-label="金色の葉の装飾"></div>
  <div class="leaf leaf--mid-right" role="img" aria-label="金色の葉の装飾"></div>
  <div class="leaf leaf--mid-left" role="img" aria-label="金色の葉の装飾"></div>
  <div class="leaf leaf--bottom-right" role="img" aria-label="金色の葉の装飾"></div>

  <header class="brand">
    <span class="brand__name">Stella Girls Bar</span><span class="brand__mark"></span>
  </header>

  <p class="offer-lead">飲み放題 1時間</p>
  <p class="offer-price">2,500yen〜</p>
  <div class="offer-rule"></div>

  <section class="menu">
    <h2 class="menu__title">MENU</h2>
    <p class="menu__item">ビール、超炭酸ハイボール</p>
    <p class="menu__item">サワー、ソフトドリンク</p>
  </section>

  <div class="figure" role="img" aria-label="ドレス姿の女性のシルエット"></div>

  <div class="map" role="img" aria-label="店舗周辺の案内地図"></div>

  <section class="info">
    <p class="info__hours">OPEN 20:00〜LAST</p>
    <p class="info__karaoke">カラオケ完備</p>
    <p class="info__contact-lead">お問い合わせ、ご予約はこちらまで</p>
    <p class="info__tel">TEL 043-518-2264</p>
    <p class="info__address">千葉県浦安市北栄2-7-14ミナトコート305</p>
  </section>
</main>
</body>
</html>
```